Cedar Brook Stables, LLC

Equestrian business card to promote equine retirement, farm sitting, short term board. Located in Aiken, SC.
Updated color schemes.
Contact Information for Business Card
Contact info, description of work.
Colors
0094D4
00A9DD
6FCCEA
C7EBF8
E9F6FB
59FF00
82FF00
B8FF75
E3FFCB
F4FFEA
F0912C
F2A743
F7CA91
FBE8D2
FDF5EE

```html
<!DOCTYPE html>
<html lang="en">
<head>
<meta charset="utf-8">
<title>Cedar Brook Stables — Business Card</title>
<link rel="stylesheet" href="https://fonts.googleapis.com/css2?family=Poppins:wght@400;500;600;700&display=swap">
<style>
  :root {
    --page-bg: #e4e4e4;
    --card-white: #ffffff;
    --card-yellow: #fdd73d;
    --ink: #222222;
    --green: #1e7d1e;
    --divider: #444444;
  }
  * { box-sizing: border-box; margin: 0; padding: 0; }
  html, body {
    width: 1200px; height: 930px; overflow: hidden;
    background: var(--page-bg);
    font-family: "Poppins", sans-serif;
    color: var(--ink);
  }
  .sheet {
    width: 1200px; height: 930px;
    display: flex; flex-direction: column; align-items: center; justify-content: center;
    gap: 44px;
  }
  .card {
    position: relative;
    width: 700px; height: 400px;
    box-shadow: 0 4px 14px rgba(0,0,0,0.12);
  }
  .card--front { background: var(--card-white); }
  .card--back { background: var(--card-yellow); }

  .brand {
    position: absolute; left: 50%; transform: translateX(-50%);
    display: flex; align-items: center; gap: 14px; white-space: nowrap;
  }
  .brand__dot {
    width: 46px; height: 46px; border-radius: 50%;
    border: 3px solid var(--green);
  }
  .brand__name {
    font-weight: 600; font-size: 26px; letter-spacing: 2px;
    color: var(--ink); text-transform: uppercase;
  }
  .card--front .brand { top: 62px; }
  .card--back .brand { top: 150px; }

  .person {
    position: absolute; top: 150px; left: 0; right: 0; text-align: center;
  }
  .person__name { font-weight: 600; font-size: 24px; letter-spacing: 1px; text-transform: uppercase; }
  .person__role { font-weight: 400; font-size: 15px; color: var(--green); letter-spacing: 1px; text-transform: uppercase; }

  .details {
    position: absolute; top: 245px; left: 0; right: 0;
    display: flex; justify-content: center; align-items: stretch; gap: 22px;
  }
  .address { text-align: right; font-size: 16px; line-height: 1.5; }
  .details__rule { width: 1px; background: var(--divider); }
  .contacts { list-style: none; font-size: 17px; line-height: 1.5; }
  .contacts li { display: flex; align-items: center; gap: 8px; }
  .contacts svg { width: 15px; height: 15px; flex: none; }

  .services {
    position: absolute; bottom: 54px; left: 0; right: 0; text-align: center;
    font-weight: 600; font-size: 18px; letter-spacing: 0.5px;
  }
  .services span { margin: 0 10px; }
</style>
</head>
<body>
<main class="sheet">
  <section class="card card--front" aria-label="Business card front">
    <div class="brand">
      <span class="brand__dot"></span>
      <span class="brand__name">Cedar Brook Stables, LLC</span>
    </div>
    <div class="person">
      <p class="person__name">Daniel Hayes</p>
      <p class="person__role">Managing Director</p>
    </div>
    <div class="details">
      <p class="address">118, Whiskey Road<br>Aiken SC<br>29801, USA</p>
      <span class="details__rule"></span>
      <ul class="contacts">
        <li>
          <svg viewBox="0 0 16 16" aria-hidden="true"><path fill="#1e7d1e" d="M3.6 1.2l2.3 2.6-1.2 1.8c.9 2 2.4 3.5 4.4 4.4l1.8-1.2 2.6 2.3-1.4 2.3C7 13.2 2.8 9 1.3 2.6z"/></svg>
          803-555 014 27
        </li>
        <li>
          <svg viewBox="0 0 16 16" aria-hidden="true"><rect x="1" y="3" width="14" height="10" fill="#1e7d1e"/><path d="M1.5 3.5L8 9l6.5-5.5" stroke="#fff" stroke-width="1.3" fill="none"/></svg>
          hello@cedarbrook.com
        </li>
        <li>
          <svg viewBox="0 0 16 16" aria-hidden="true"><circle cx="8" cy="8" r="7" fill="#1e7d1e"/><path d="M1 8h14M8 1c-3 3.5-3 10.5 0 14M8 1c3 3.5 3 10.5 0 14" stroke="#fff" stroke-width="1" fill="none"/></svg>
          www.cedarbrook.com
        </li>
      </ul>
    </div>
  </section>

  <section class="card card--back" aria-label="Business card back">
    <div class="brand">
      <span class="brand__dot"></span>
      <span class="brand__name">Cedar Brook Stables, LLC</span>
    </div>
    <p class="services">Short Term Board<span>|</span>Farm Sitting<span>|</span>Equine Retirement</p>
  </section>
</main>
</body>
</html>
```